Flyer for Lawnmowing and gardening business

We are a lawn mowing and gardening business needing a flyer designed listing our services and business info.
The flyer should include all business information and contact details as below.

Lawn mowing
Gardening
Green waste removal
Pruning
Weeding
Vegetable Garden Creation

Phone number:0481657240

As well as the logo provided

Target Market(s)

Local people wanting someone to care for their garden.

Industry/Entity Type

Gardener

Font styles to use
Serif

Requirements
Must have
• Business Logo
• All business info and services provided. EG
• Lawn mowing
• Gardening
• Green waste removal
• Pruning
• Weeding
• Vegetable Garden Creation
• Phone number:0481657240
Nice to have
• Earthy tones, clean and simple flyer design

```html
<!DOCTYPE html>
<html lang="en">
<head>
<meta charset="utf-8">
<title>Brookhollow Yards – Flyer</title>
<link rel="stylesheet" href="https://fonts.googleapis.com/css2?family=Oswald:wght@300;400;600&display=swap">
<style>
  :root {
    --accent-green: #9fd23a;
    --earth-dark: #5d4a2e;
    --maroon: #6b1f2a;
    --maroon-band: #5a1a22;
    --charcoal: #4a4645;
    --crimson: #c2243d;
    --pine: #1e6b3a;
    --lime: #d8ec2a;
    --pale-pink: #f2c9cf;
    --paper: #ffffff;
  }
  * { margin: 0; padding: 0; box-sizing: border-box; }
  html, body { width: 1200px; height: 2536px; overflow: hidden; background: var(--paper); }
  .flyer { position: relative; width: 1200px; height: 2536px; overflow: hidden; background: var(--paper); }
  .backdrop { position: absolute; inset: 0; }
  .services { position: absolute; top: 70px; left: 0; width: 1200px; text-align: center; font-family: "Oswald", sans-serif; text-transform: uppercase; line-height: 1; }
  .services p { margin: 0; }
  .svc-main { font-weight: 600; font-size: 130px; letter-spacing: 2px; }
  .svc-sub { font-weight: 300; font-size: 92px; letter-spacing: 1px; margin-top: 2px; }
  .lawn, .weeding { color: var(--maroon); }
  .gardening { color: var(--charcoal); margin-top: 22px; }
  .green, .waste { color: var(--crimson); }
  .green { margin-top: 16px; }
  .pruning { color: var(--pine); margin-top: 22px; }
  .weeding { margin-top: 16px; }
  .vegetable, .creation { color: var(--lime); }
  .vegetable { margin-top: 16px; }
  .phone { position: absolute; left: 400px; top: 1720px; transform: rotate(-10deg); transform-origin: left top; font-family: "Oswald", sans-serif; color: var(--pale-pink); line-height: 1; }
  .phone-label { font-weight: 400; font-size: 66px; letter-spacing: 3px; }
  .phone-number { font-weight: 300; font-size: 144px; letter-spacing: 5px; margin-top: 6px; }
  .brand { position: absolute; top: 2330px; left: 0; width: 1200px; text-align: center; }
  .brand-name { font-family: "Oswald", sans-serif; font-weight: 400; font-size: 96px; color: var(--maroon); letter-spacing: 3px; line-height: 1; }
</style>
</head>
<body>
<div class="flyer">
  <svg class="backdrop" width="1200" height="2536" viewBox="0 0 1200 2536" xmlns="http://www.w3.org/2000/svg">
    <defs>
      <linearGradient id="lawnGrad" x1="0" y1="0" x2="1" y2="1">
        <stop offset="0" stop-color="#9fcf4a"/>
        <stop offset="0.5" stop-color="#6fac2c"/>
        <stop offset="1" stop-color="#3f7a18"/>
      </linearGradient>
      <linearGradient id="siteGrad" x1="0" y1="0" x2="0" y2="1">
        <stop offset="0" stop-color="#5f7a42"/>
        <stop offset="0.3" stop-color="#a87a52"/>
        <stop offset="0.6" stop-color="#c98a5a"/>
        <stop offset="1" stop-color="#b7764a"/>
      </linearGradient>
    </defs>
    <rect class="site-photo" role="img" aria-label="Earthworks site with graders levelling red soil below a wooded hillside" x="0" y="1000" width="1200" height="1300" fill="url(#siteGrad)"/>
    <polygon class="lawn-photo" role="img" aria-label="Freshly mowed striped green lawn" points="0,0 1200,0 1200,1070 0,1460" fill="url(#lawnGrad)"/>
    <polygon class="accent-stripe" points="0,1440 1200,1050 1200,1090 0,1485" fill="var(--accent-green)"/>
    <polygon class="phone-band" points="376,1810 1200,1540 1200,1750 376,2000" fill="var(--maroon-band)" fill-opacity="0.92"/>
    <polygon class="footer-edge" points="0,2150 1200,1760 1200,1785 0,2180" fill="var(--earth-dark)"/>
    <polygon class="footer" points="0,2180 1200,1785 1200,2536 0,2536" fill="var(--paper)"/>
  </svg>

  <div class="services">
    <p class="svc-main lawn">Lawn</p>
    <p class="svc-sub lawn">Mowing</p>
    <p class="svc-main gardening">Gardening</p>
    <p class="svc-main green">Green</p>
    <p class="svc-sub waste">Waste Removal</p>
    <p class="svc-main pruning">Pruning</p>
    <p class="svc-main weeding">Weeding</p>
    <p class="svc-main vegetable">Vegetable</p>
    <p class="svc-sub creation">GardenCreation</p>
  </div>

  <div class="phone">
    <p class="phone-label">PHONE NO.</p>
    <p class="phone-number">0481657240</p>
  </div>

  <div class="brand">
    <p class="brand-name">BROOKHOLLOW YARDS</p>
  </div>
</div>
</body>
</html>
```